Picture Ads

We need some banner ads for our home business opportunity, we are evolving from text to picture ads. I have added some examples of what other distributors are using. We are looking for something really eye catching with some good key words and nice bright colours and to include our photo (attached)
Key words to include:
Booming online business
Personal Development and Leadership Industry
Earn an executive income from home
Simple 3 step system
Make up to $5,000 per sale
Not MLM
The size needs to be: 1000 x 35 pixels
13.9 x 4.75 Inches
35.3 x 11.1 cm
I think different platforms accept different sizes, not too familiar with it yet, any guidance welcome. I've clicked project for 2 days if that is to prioritise the order?
Many thanks,
Maren

Industry/Entity Type

Business

```html
<!DOCTYPE html>
<html lang="en">
<head>
<meta charset="utf-8">
<title>Booming Online Business Banner</title>
<link href="https://fonts.googleapis.com/css2?family=Roboto+Condensed:wght@300;400;700;900&family=Oswald:wght@500;700&display=swap" rel="stylesheet">
<style>
  :root {
    --royal: #1f35b8;
    --navy: #1a2a9e;
    --sky: #7d97ec;
    --sky-soft: #a9bdf4;
    --aqua: #b6eef6;
    --lilac: #dcdcf4;
    --paper: #f7f9ff;
    --ink: #111111;
    --white: #ffffff;
  }
  html, body {
    margin: 0;
    padding: 0;
    width: 1200px;
    height: 378px;
    overflow: hidden;
    background: var(--white);
  }
  .banner {
    position: relative;
    width: 1200px;
    height: 378px;
    overflow: hidden;
    background: var(--paper);
    font-family: "Roboto Condensed", "Arial Narrow", sans-serif;
  }
  .waves {
    position: absolute;
    inset: 0;
  }
  .portrait {
    position: absolute;
    left: 0;
    top: 0;
    width: 324px;
    height: 322px;
    background: radial-gradient(ellipse at 35% 40%, #d9a08a 0%, #8a4a3a 45%, #3a1f1c 100%);
  }
  .steps-label {
    position: absolute;
    left: 0;
    top: 320px;
    width: 338px;
    height: 58px;
    background: var(--royal);
    color: var(--white);
    font-weight: 700;
    font-size: 27px;
    display: flex;
    align-items: center;
    justify-content: center;
    gap: 7px;
    white-space: nowrap;
  }
  .steps-label .step-count {
    font-size: 46px;
    font-weight: 900;
    line-height: 1;
  }
  .headline {
    position: absolute;
    left: 340px;
    width: 820px;
    top: 28px;
    margin: 0;
    text-align: center;
    color: var(--navy);
    font-weight: 700;
    font-size: 66px;
    line-height: 1;
    white-space: nowrap;
  }
  .industry {
    position: absolute;
    left: 340px;
    width: 820px;
    top: 148px;
    margin: 0;
    text-align: center;
    color: var(--ink);
    font-family: "Oswald", "Arial Narrow", sans-serif;
    font-weight: 500;
    font-size: 34px;
    line-height: 1;
    white-space: nowrap;
  }
  .income {
    position: absolute;
    left: 340px;
    width: 820px;
    top: 212px;
    margin: 0;
    text-align: center;
    color: var(--ink);
    font-family: "Oswald", "Arial Narrow", sans-serif;
    font-weight: 700;
    line-height: 1;
    white-space: nowrap;
  }
  .income .big { font-size: 46px; }
  .income .small { font-size: 30px; }
  .income .biggest { font-size: 52px; }
  .offer {
    position: absolute;
    left: 360px;
    top: 282px;
    height: 90px;
    display: flex;
    align-items: center;
    gap: 12px;
    color: var(--ink);
    font-weight: 300;
    font-size: 52px;
    white-space: nowrap;
    letter-spacing: -1px;
  }
  .offer .amount {
    font-weight: 900;
    font-size: 68px;
    color: var(--white);
    background: var(--royal);
    border-radius: 22px;
    padding: 0 8px;
    line-height: 1.1;
    -webkit-text-stroke: 3px var(--navy);
    paint-order: stroke fill;
    letter-spacing: 0;
  }
  .not-mlm {
    position: absolute;
    left: 998px;
    top: 272px;
    width: 202px;
    height: 106px;
    background: var(--royal);
    color: var(--white);
    font-weight: 900;
    font-size: 40px;
    display: flex;
    align-items: center;
    justify-content: center;
    gap: 8px;
    white-space: nowrap;
  }
  .not-mlm .mlm { font-size: 48px; }
</style>
</head>
<body>
  <div class="banner">
    <svg class="waves" width="1200" height="378" viewBox="0 0 1200 378" aria-hidden="true">
      <path d="M0 0 H1200 V190 C1080 240 920 150 760 145 C600 140 470 200 320 215 V0 Z" fill="var(--sky)"/>
      <path d="M320 215 C470 200 600 140 760 145 C920 150 1080 240 1200 190 V215 C1060 260 920 185 760 180 C600 175 480 230 320 240 Z" fill="var(--sky-soft)" opacity="0.7"/>
      <path d="M320 300 C480 250 640 235 820 250 C960 262 1080 240 1200 215 V250 C1060 285 940 300 800 285 C640 270 480 290 320 330 Z" fill="var(--aqua)"/>
      <path d="M0 340 C200 320 300 300 420 310 C560 322 640 378 760 378 H0 Z" fill="var(--lilac)"/>
    </svg>

    <div class="portrait" role="img" aria-label="Photo of the two business owners smiling together"></div>
    <div class="steps-label">Simple <span class="step-count">3</span> step system</div>

    <h1 class="headline">Booming ONLINE Business</h1>
    <p class="industry">Personal Development and Leadership Industry</p>
    <p class="income"><span class="big">Earn</span> <span class="small">an executive</span> <span class="biggest">income</span> <span class="small">from</span> <span class="big">home</span></p>

    <div class="offer">
      <span>Make up to</span>
      <span class="amount">$5,000</span>
      <span>per sale</span>
    </div>

    <div class="not-mlm"><span>Not</span><span class="mlm">MLM</span></div>
  </div>
</body>
</html>
```